Fatigued and Overloaded by COVID Messages? We need original illustrations to show that.

Everywhere you look there are messages about COVID. That is leading many people to feel fatigued and overloaded by the messages.

We surveyed U.S. adults March 20th - 24th, 2020 and measured message fatigue, information overload, perceived repetition, and perceived exaggeration. Here is how participants responded:

When it comes to coronavirus . . .
55% feel exhausted by all the messages.
54% feel overloaded by the amount of information.
51% feel that the messages are repetitive.
47% feel like messages exaggerate how bad it is.

In other words, almost half of U.S. adults show signs of message fatigue, information overload, perceived message repetition, and perceived message exaggeration.

We will continue to survey 400 adults every week for the next 16 weeks. Each time we will measure message fatigue, information overload, perceived repetition, and perceived exaggeration. We expect that it will increase over time.

What are we looking for? We need innovative and original illustrations that attempt to communicate these findings. The illustrations would visualize message fatigue, information overload, perceived message repetition, and perceived message exaggeration.

What sort of visual are we looking for? Our preference is for an original illustration (or set of illustrations). Our preference is for creative and powerful illustrations, but we are also open to the creative and well-executed infographics.

We need these images fast . We will award monetary prizes to the 3 best designs. If we like more than that, then we might purchase more (e.g., in past contests, we have purchased as many as 30 designs).

What we will need:
(1) The illustrations must be original and we will need the photoshop and/or illustrator files for all artwork. (By original, we mean that the illustrations are 100% created by you. Our organization requires that we utilize only original illustrated work. We have had issues with free imagery being pirated and reposted as free. We sidestep that issue by just having everything created.)

(2) The illustration should say, somewhere: "Based on a survey of 400 U.S. adults conducted March 20 - 24th, 2020."

(3) We will have almost 4 months worth of data by the time this is done. In other words, the illustrations might be able to help us present that weekly data.

(4) We have conducted other Artvendo projects. It might be helpful to examine designs we liked in the past. For example, here is another COVID project we just finished:

https://jobs.artvendo-example.com/job/5162048

Target Market(s)

U.S. adults

Requirements
Must have
• Original illustrations. Mobile friendly design. People will view this on their smartphones.
Nice to have
• A design that we can use to communicate the data across time.

```html
<!DOCTYPE html>
<html lang="en">
<head>
<meta charset="utf-8">
<title>COVID Message Fatigue</title>
<link href="https://fonts.googleapis.com/css2?family=Bebas+Neue&family=Roboto:wght@100&display=swap" rel="stylesheet">
<style>
  :root {
    --pink: #ff0066;
    --mint: #33cc99;
    --sage: #99cc99;
    --sky: #99cccc;
    --ink: #222222;
    --grey: #bbbbbb;
    --icon: #7a7a7a;
    --paper: #ffffff;
  }
  html, body { margin: 0; padding: 0; overflow: hidden; background: var(--paper); }
  .poster {
    position: relative;
    width: 849px;
    height: 1200px;
    overflow: hidden;
    background: var(--paper);
    font-family: "Bebas Neue", "Oswald", sans-serif;
    color: var(--ink);
  }
  .abs { position: absolute; }
  .intro-band {
    left: 286px; top: 0; width: 563px; height: 120px;
    background: var(--pink);
  }
  .intro-text {
    left: 286px; top: 28px; width: 563px;
    margin: 0; text-align: center;
    color: var(--paper); font-size: 13.5px; line-height: 21px; letter-spacing: 0.2px;
  }
  .figure { border-radius: 40px; }
  .figure-wave { left: 44px; top: 8px; width: 256px; height: 228px;
    background: linear-gradient(180deg, #f3c9a0 0%, #9ccfd0 45%, #7f8c8c 100%); }
  .figure-umbrella { left: 572px; top: 316px; width: 264px; height: 332px;
    background: linear-gradient(180deg, #868686 0%, #868686 38%, #9ccfd0 60%, #7f8c8c 100%); }
  .figure-cheer { left: 340px; top: 960px; width: 204px; height: 224px;
    background: linear-gradient(180deg, #f3c9a0 0%, #9ccfd0 50%, #7f8c8c 100%); }
  .ground { height: 2px; background: #777; }
  .ground-left { left: 48px; top: 208px; width: 188px; }
  .ground-right { left: 596px; top: 625px; width: 200px; }
  .title-covid {
    left: 292px; top: 200px; margin: 0;
    font-size: 82px; line-height: 1; color: var(--grey); font-weight: 400;
  }
  .title-mark {
    left: 472px; top: 108px;
    font-family: "Roboto", sans-serif; font-weight: 100;
    font-size: 200px; line-height: 1; color: var(--grey);
  }
  .media-icon { width: 26px; height: 26px; }
  .stat-lead, .stat-label {
    left: 34px; margin: 0; font-size: 28px; line-height: 1; font-weight: 400; white-space: nowrap;
  }
  .bar {
    left: 30px; width: 529px; height: 42px;
    border: 1px solid #555; box-sizing: border-box; background: var(--paper);
  }
  .bar-fill { height: 100%; }
  .virus-pink { left: 624px; top: 736px; width: 196px; height: 204px; border-radius: 50%; background: var(--pink); }
  .source-band { left: 0; top: 838px; width: 849px; height: 148px; background: var(--mint); }
  .source-text {
    left: 0; top: 883px; width: 849px; margin: 0; text-align: center;
    color: var(--paper); font-size: 34px; line-height: 40px;
  }
  .virus-grey { left: 20px; top: 932px; width: 198px; height: 200px; border-radius: 50%; background: #cccccc; }
</style>
</head>
<body>
<main class="poster">
  <div class="abs figure figure-wave" role="img" aria-label="Illustration of a bearded man in a face mask leaning on the banner"></div>
  <div class="abs ground ground-left"></div>

  <div class="abs intro-band"></div>
  <p class="abs intro-text">We surveyed U.S. adults March 20th - 24th, 2020 and measured message fatigue,<br>information overload, perceived repetition, and perceived exaggeration.<br>Here is how participants responded:</p>

  <h1 class="abs title-covid">COVID</h1>
  <span class="abs title-mark" aria-hidden="true">?</span>

  <svg class="abs media-icon" style="left:620px;top:160px" viewBox="0 0 24 24" aria-hidden="true"><rect x="4" y="2" width="16" height="20" rx="1" fill="none" stroke="var(--icon)" stroke-width="2"/><path d="M8 2v20M16 2v20M4 8h4M4 12h4M4 16h4M16 8h4M16 12h4M16 16h4" stroke="var(--icon)" stroke-width="1.5"/></svg>
  <svg class="abs media-icon" style="left:740px;top:186px" viewBox="0 0 24 24" aria-hidden="true"><rect x="6" y="2" width="12" height="20" rx="2" fill="none" stroke="var(--icon)" stroke-width="2"/><circle cx="12" cy="19" r="1" fill="var(--icon)"/></svg>
  <svg class="abs media-icon" style="left:592px;top:226px;width:32px;height:32px" viewBox="0 0 24 24" aria-hidden="true"><path d="M8 3l4 4 4-4" fill="none" stroke="var(--icon)" stroke-width="2"/><rect x="3" y="7" width="18" height="13" rx="3" fill="none" stroke="var(--icon)" stroke-width="2.5"/></svg>
  <svg class="abs media-icon" style="left:778px;top:230px" viewBox="0 0 24 24" aria-hidden="true"><path d="M6 8l10-5" stroke="var(--icon)" stroke-width="2"/><rect x="2" y="8" width="20" height="12" rx="2" fill="none" stroke="var(--icon)" stroke-width="2"/><circle cx="8" cy="14" r="3" fill="var(--icon)"/><rect x="14" y="12" width="5" height="4" fill="var(--icon)"/></svg>
  <svg class="abs media-icon" style="left:668px;top:248px" viewBox="0 0 24 24" aria-hidden="true"><path d="M3 9h5l9-5v16l-9-5H3z" fill="var(--icon)"/><path d="M6 15l2 6h3l-2-6" fill="var(--icon)"/></svg>
  <svg class="abs media-icon" style="left:726px;top:280px" viewBox="0 0 24 24" aria-hidden="true"><rect x="2" y="5" width="20" height="14" rx="2" fill="var(--icon)"/><path d="M3 7l9 6 9-6" fill="none" stroke="#fff" stroke-width="1.6"/></svg>
  <svg class="abs media-icon" style="left:600px;top:302px" viewBox="0 0 24 24" aria-hidden="true"><circle cx="12" cy="12" r="9" fill="none" stroke="var(--icon)" stroke-width="2"/><ellipse cx="12" cy="12" rx="4" ry="9" fill="none" stroke="var(--icon)" stroke-width="1.6"/><path d="M3 12h18M5 7.5h14M5 16.5h14" stroke="var(--icon)" stroke-width="1.6"/></svg>

  <div class="abs figure figure-umbrella" role="img" aria-label="Illustration of a masked bearded man sheltering under a grey umbrella from falling media icons"></div>
  <div class="abs ground ground-right"></div>

  <h2 class="abs stat-lead" style="top:314px">When it comes to coronavirus . . .</h2>

  <div class="abs bar" style="top:349px"><div class="bar-fill" style="width:284px;background:var(--pink)"></div></div>
  <p class="abs stat-label" style="top:414px">55% feel exhausted by all the messages.</p>

  <div class="abs bar" style="top:451px"><div class="bar-fill" style="width:269px;background:var(--mint)"></div></div>
  <p class="abs stat-label" style="top:517px">54% feel overloaded by the amount of information.</p>

  <div class="abs bar" style="top:562px"><div class="bar-fill" style="width:264px;background:var(--sage)"></div></div>
  <p class="abs stat-label" style="top:618px">51% feel that the messages are repetitive.</p>

  <div class="abs bar" style="top:666px"><div class="bar-fill" style="width:249px;background:var(--sky)"></div></div>
  <p class="abs stat-label" style="top:722px">47% feel like messages exaggerate how bad it is.</p>

  <div class="abs virus-pink" role="img" aria-label="Pink coronavirus particle illustration"></div>

  <div class="abs source-band"></div>
  <p class="abs source-text">Based on a survey of 400 U.S.<br>adults conducted March 20 - 24th, 2020</p>

  <div class="abs virus-grey" role="img" aria-label="Grey coronavirus particle illustration"></div>
  <div class="abs figure figure-cheer" role="img" aria-label="Illustration of a masked bearded man holding up the source banner"></div>
</main>
</body>
</html>
```